Stationary for a computer tech, hardware selling & website building & hosting for smb's
Pavillon Informatique
Professional
Mathieu Ostrowel
Directeur associé
4187 Boul. Lanvoisier Est
Montréal (Qc) H7T 8W2
514.555.0148 p.317
mathieu@pavillon-exemple.ca
www.pavillon-exemple.ca
Logo on white background
Logo on black background

```html
<!DOCTYPE html>
<html lang="fr">
<head>
<meta charset="utf-8">
<title>Pavillon Informatique – cartes professionnelles</title>
<link rel="stylesheet" href="https://fonts.googleapis.com/css2?family=Source+Sans+3:wght@400;600;700&display=swap">
<style>
  :root {
    --green: #7cc142;
    --green-dark: #5fa02c;
    --ink: #1e1e1e;
    --black-card: #0f0f0f;
    --paper: #ffffff;
    --stage: #e9ebee;
    --grey-line: #3a3a3a;
    --muted: #555555;
  }
  * { box-sizing: border-box; margin: 0; padding: 0; }
  html, body {
    width: 1200px; height: 1009px; overflow: hidden;
    background: var(--stage);
    font-family: "Source Sans 3", "Helvetica Neue", Arial, sans-serif;
  }
  .canvas { position: relative; width: 1200px; height: 1009px; }
  .card {
    position: absolute; left: 210px;
    width: 780px; height: 446px;
    border-radius: 20px; overflow: hidden;
    box-shadow: 0 6px 18px rgba(0,0,0,0.15);
  }
  .card--light { top: 40px; background: var(--paper); color: var(--ink); }
  .card--dark { top: 523px; background: var(--black-card); color: #f2f2f2; }
  .card__swoosh { position: absolute; inset: 0; width: 100%; height: 100%; }
  .brand {
    position: absolute; left: 48px; top: 40px;
    display: flex; align-items: center; gap: 16px;
  }
  .brand__dot {
    width: 58px; height: 58px; border-radius: 50%;
    background: var(--green);
  }
  .brand__name {
    font-size: 38px; font-weight: 700; letter-spacing: -0.5px;
  }
  .card--light .brand__name { color: var(--ink); }
  .card--dark .brand__name { color: #ffffff; }
  .contact {
    position: absolute; left: 52px; top: 136px;
    list-style: none; font-size: 16px; line-height: 25px;
  }
  .contact li { display: flex; align-items: center; gap: 9px; }
  .contact svg { width: 13px; height: 13px; flex: none; }
  .contact .address { padding-left: 0; }
  .person {
    position: absolute; right: 48px; bottom: 34px;
    text-align: right; color: var(--ink);
  }
  .person__name { font-size: 27px; font-weight: 600; line-height: 1.1; }
  .person__title { font-size: 17px; font-weight: 600; }
</style>
</head>
<body>
<main class="canvas">

  <!-- Light version -->
  <section class="card card--light">
    <svg class="card__swoosh" viewBox="0 0 780 446" preserveAspectRatio="none" aria-hidden="true">
      <path d="M0,446 L0,385 C250,335 520,300 780,255 L780,446 Z" fill="var(--green)"/>
      <path d="M0,362 C260,305 520,270 780,228 L780,244 C520,287 260,322 0,376 Z" fill="var(--grey-line)"/>
    </svg>
    <div class="brand">
      <span class="brand__dot"></span>
      <span class="brand__name">Pavillon Informatique</span>
    </div>
    <ul class="contact">
      <li class="address">4187 Boul. Lanvoisier Est, Montréal (Qc) H7T 8W2</li>
      <li><svg viewBox="0 0 12 12"><path d="M2 1h3l1 3-2 1a6 6 0 0 0 3 3l1-2 3 1v3c-6 0-9-3-9-9z" fill="var(--green)"/></svg>514.555.0148 p.317</li>
      <li><svg viewBox="0 0 12 12"><path d="M2 1h3l1 3-2 1a6 6 0 0 0 3 3l1-2 3 1v3c-6 0-9-3-9-9z" fill="var(--green)"/></svg>514.555.0193</li>
      <li><svg viewBox="0 0 12 12"><rect x="1" y="2" width="10" height="8" fill="var(--green)"/></svg>514.555.0172</li>
      <li><svg viewBox="0 0 12 12"><rect x="1" y="2.5" width="10" height="7" fill="var(--green)"/><path d="M1 3l5 4 5-4" stroke="#fff" fill="none"/></svg>mathieu@pavillon-exemple.ca</li>
      <li><svg viewBox="0 0 12 12"><circle cx="6" cy="6" r="5" fill="var(--green)"/></svg>www.pavillon-exemple.ca</li>
    </ul>
    <div class="person">
      <p class="person__name">Mathieu Ostrowel</p>
      <p class="person__title">Directeur Associé</p>
    </div>
  </section>

  <!-- Dark version -->
  <section class="card card--dark">
    <svg class="card__swoosh" viewBox="0 0 780 446" preserveAspectRatio="none" aria-hidden="true">
      <path d="M0,446 L0,385 C250,335 520,300 780,255 L780,446 Z" fill="var(--green)"/>
      <path d="M0,362 C260,305 520,270 780,228 L780,244 C520,287 260,322 0,376 Z" fill="#8a8a8a"/>
    </svg>
    <div class="brand">
      <span class="brand__dot"></span>
      <span class="brand__name">Pavillon Informatique</span>
    </div>
    <ul class="contact">
      <li class="address">4187 Boul. Lanvoisier Est, Montréal (Qc) H7T 8W2</li>
      <li><svg viewBox="0 0 12 12"><path d="M2 1h3l1 3-2 1a6 6 0 0 0 3 3l1-2 3 1v3c-6 0-9-3-9-9z" fill="var(--green)"/></svg>514.555.0148 p.317</li>
      <li><svg viewBox="0 0 12 12"><path d="M2 1h3l1 3-2 1a6 6 0 0 0 3 3l1-2 3 1v3c-6 0-9-3-9-9z" fill="var(--green)"/></svg>514.555.0193</li>
      <li><svg viewBox="0 0 12 12"><rect x="1" y="2" width="10" height="8" fill="var(--green)"/></svg>514.555.0172</li>
      <li><svg viewBox="0 0 12 12"><rect x="1" y="2.5" width="10" height="7" fill="var(--green)"/><path d="M1 3l5 4 5-4" stroke="#0f0f0f" fill="none"/></svg>mathieu@pavillon-exemple.ca</li>
      <li><svg viewBox="0 0 12 12"><circle cx="6" cy="6" r="5" fill="var(--green)"/></svg>www.pavillon-exemple.ca</li>
    </ul>
    <div class="person">
      <p class="person__name">Mathieu Ostrowel</p>
      <p class="person__title">Directeur Associé</p>
    </div>
  </section>

</main>
</body>
</html>
```